Volren Goods Ltd Stationery Design Project

hi we need to design business cards, letter head, complimentary slips, scribble pads, note pads, envelopes for volren goods ltd.

please see business cards details

Kelvin Obutu

P.O Box 41873 -00312 Nairobi - Kenya
Tel: +254-733-218-904
Email: volrengoods@mailvexo.com

company name should appear on all stationery : Volren Goods Ltd

Industry/Entity Type

Business

Requirements
Must have
• kindly stick to colours in the logo

```html
<!DOCTYPE html>
<html lang="en">
<head>
<meta charset="utf-8">
<title>Volren Goods Ltd – Letterhead</title>
<link href="https://fonts.googleapis.com/css2?family=Fredoka:wght@400;500;600&display=swap" rel="stylesheet">
<style>
  :root {
    --paper: #e6e7e8;
    --orange: #f7941d;
    --blue: #283b8f;
    --ink: #231f20;
    --faint: rgba(247, 148, 29, 0.07);
  }
  html, body {
    margin: 0;
    padding: 0;
    overflow: hidden;
  }
  .letterhead {
    position: relative;
    width: 848px;
    height: 1200px;
    background: var(--paper);
    overflow: hidden;
    font-family: "Fredoka", sans-serif;
  }
  .brand-name {
    position: absolute;
    left: 50px;
    top: 72px;
    margin: 0;
    display: flex;
    align-items: center;
    gap: 10px;
    font-size: 34px;
    font-weight: 600;
    line-height: 1;
    color: var(--orange);
    text-transform: uppercase;
  }
  .brand-dot {
    width: 20px;
    height: 20px;
    border-radius: 50%;
    background: var(--orange);
  }
  .contact {
    position: absolute;
    left: 636px;
    top: 48px;
    color: var(--ink);
  }
  .contact-company {
    margin: 0 0 6px;
    font-size: 20px;
    font-weight: 500;
    color: var(--blue);
    line-height: 1.1;
  }
  .contact-line {
    margin: 0;
    font-size: 10.5px;
    line-height: 15px;
  }
  .band {
    position: absolute;
    left: 0;
    width: 100%;
  }
  .band-orange { top: 158px; height: 23px; background: var(--orange); }
  .band-blue { top: 189px; height: 22px; background: var(--blue); }
  .backdrop-name {
    position: absolute;
    left: 0;
    top: 560px;
    width: 100%;
    margin: 0;
    text-align: center;
    font-size: 150px;
    font-weight: 600;
    line-height: 1.05;
    color: var(--faint);
    text-transform: uppercase;
  }
  .footer-wave {
    position: absolute;
    left: 0;
    bottom: 0;
    width: 848px;
    height: 100px;
  }
</style>
</head>
<body>
<div class="letterhead">
  <p class="brand-name"><span class="brand-dot"></span>Volren Goods</p>

  <div class="contact">
    <p class="contact-company">Volren Goods Ltd</p>
    <p class="contact-line">Nairobi - Kenya</p>
    <p class="contact-line">P.O Box 41873 -00312</p>
    <p class="contact-line">Tel: +254-733-218-904</p>
    <p class="contact-line">Email: volrengoods@mailvexo.com</p>
  </div>

  <div class="band band-orange"></div>
  <div class="band band-blue"></div>

  <p class="backdrop-name" aria-hidden="true">Volren<br>Goods</p>

  <svg class="footer-wave" viewBox="0 0 848 100" preserveAspectRatio="none" aria-hidden="true">
    <path d="M0 30 C 200 48, 500 20, 700 8 C 770 4, 820 6, 848 12 L848 100 L0 100 Z" fill="var(--orange)"/>
    <path d="M0 48 C 220 64, 520 40, 720 28 C 790 24, 830 26, 848 32 L848 100 L0 100 Z" fill="var(--blue)"/>
  </svg>
</div>
</body>
</html>
```